RevelHubQZ Business Cards

Front
Has logo with a design. Website address (www.revelhubqz.example)
Has slogan (discover nightlife)
Has phone number (5129873304)
Should be bold and stands out.

Back
Has details about what we offer.

Events
Search upcoming events
Submit events
Party Image Gallery
View and download HQ party images
Sign up as a contributing event photographer and get paid!
Tickets
Sell your event tickets online for free!
Direct pay
No ticket fee

Target Market(s)

These cards will be handed out in clubs and events to patrons.

Industry/Entity Type

Business

Contact Information for Business Card

Should match or mirror our website in some sort of way. Visit the website to get ideas.

Requirements
Must have
• Must be designed for a 3x3 inch card.

```html
<!DOCTYPE html>
<html lang="en">
<head>
<meta charset="utf-8">
<title>RevelHubQZ Business Cards</title>
<link href="https://fonts.googleapis.com/css2?family=Open+Sans:wght@400;600;700&display=swap" rel="stylesheet">
<style>
  :root {
    --sky: #2e9fd6;
    --sky-deep: #2b98cf;
    --magenta: #e2348f;
    --paper: #ffffff;
    --stage: #3a3a3a;
    --slogan-grey: #555555;
  }
  * { margin: 0; padding: 0; box-sizing: border-box; }
  html, body { width: 1200px; height: 750px; overflow: hidden; }
  body {
    background: var(--stage);
    font-family: "Open Sans", sans-serif;
    position: relative;
  }
  .card {
    position: absolute;
    top: 166px;
    width: 416px;
    height: 416px;
    overflow: hidden;
  }
  .card--front { left: 170px; background: var(--paper); }
  .card--back { left: 619px; background: var(--sky-deep); }

  .card__wash { position: absolute; }
  .card--front .card__wash--top {
    left: 0; top: 0; width: 416px; height: 200px;
    background: linear-gradient(165deg, var(--sky) 0%, var(--sky) 30%, rgba(226, 52, 143, 0.35) 55%, rgba(255, 255, 255, 0) 80%);
  }
  .card--front .card__wash--corner {
    right: 0; bottom: 0; width: 300px; height: 240px;
    background: radial-gradient(ellipse at 100% 100%, rgba(46, 159, 214, 0.14) 0%, rgba(46, 159, 214, 0) 70%);
  }
  .card--back .card__wash--corner {
    right: 0; bottom: 0; width: 300px; height: 300px;
    background: radial-gradient(ellipse at 100% 100%, rgba(255, 255, 255, 0.16) 0%, rgba(255, 255, 255, 0) 70%);
  }

  .brand__dot { position: absolute; width: 46px; height: 46px; border-radius: 50%; }
  .brand__name {
    position: absolute; font-size: 33px; font-weight: 400;
    letter-spacing: -0.5px; line-height: 40px;
  }
  .brand__slogan {
    position: absolute; font-size: 10px; letter-spacing: 5.6px; line-height: 12px;
  }

  .card--front .brand__dot { left: 40px; top: 219px; background: var(--sky); }
  .card--front .brand__name { left: 108px; top: 222px; color: var(--sky); }
  .card--front .brand__slogan { left: 110px; top: 258px; color: var(--slogan-grey); }

  .phone {
    position: absolute; left: 44px; top: 308px;
    font-size: 41px; line-height: 52px; font-weight: 600; color: var(--sky); letter-spacing: 0.5px;
  }
  .website {
    position: absolute; left: 40px; top: 353px;
    font-size: 18.5px; line-height: 26px; font-weight: 600; color: var(--magenta);
  }

  .card--back .brand__dot { left: 42px; top: 59px; background: var(--paper); }
  .card--back .brand__name { left: 108px; top: 62px; color: var(--paper); }
  .card--back .brand__slogan { left: 110px; top: 97px; color: var(--paper); }

  .offer { position: absolute; left: 36px; top: 195px; color: var(--paper); }
  .offer__title { font-size: 17px; line-height: 22px; font-weight: 700; margin-bottom: 2px; }
  .offer__list { list-style: none; }
  .offer__list li {
    font-size: 12.6px; line-height: 17.2px; letter-spacing: -0.2px;
    padding-left: 16px; position: relative; white-space: nowrap;
  }
  .offer__list li::before {
    content: ""; position: absolute; left: 2px; top: 6px;
    width: 6px; height: 6px; border-radius: 50%; background: var(--paper);
  }
</style>
</head>
<body>

<section class="card card--front" aria-label="Card front">
  <div class="card__wash card__wash--top" role="img" aria-label="Decorative blue wave with a magenta accent across the top"></div>
  <div class="card__wash card__wash--corner" role="img" aria-label="Faint decorative pattern in pale blue and pink"></div>
  <span class="brand__dot"></span>
  <span class="brand__name">RevelHubQZ</span>
  <span class="brand__slogan">discover nightlife</span>
  <div class="phone">5129873304</div>
  <div class="website">www.revelhubqz.example</div>
</section>

<section class="card card--back" aria-label="Card back">
  <div class="card__wash card__wash--corner" role="img" aria-label="Faint decorative pattern in light blue"></div>
  <span class="brand__dot"></span>
  <span class="brand__name">RevelHubQZ</span>
  <span class="brand__slogan">discover nightlife</span>
  <div class="offer">
    <h2 class="offer__title">Events</h2>
    <ul class="offer__list">
      <li>Search upcoming events</li>
      <li>Submit events</li>
      <li>Party Image Gallery</li>
      <li>View and download HQ party images</li>
      <li>Sign up as a contributing event photographer &amp; get paid!</li>
      <li>Tickets</li>
      <li>Sell your event tickets online for free!</li>
      <li>Direct pay</li>
      <li>No ticket fee</li>
    </ul>
  </div>
</section>

</body>
</html>
```